Wealth Management Business Card

We are a professional services consulting firm that specializes in high net worth individuals over $25,000,000, executives C-suite and above, closely held businesses owners, family offices and highly compensated employees.

Our focus is on risk mitigation and tax efficient strategies. Our clients take their risk on themselves and have a proven track record generating wealth. Our directive is to preserve and protect the wealth they’ve already created.

Our company Harrowgate Advisory is geared around five directives of asset protection:
1) Legal Structuring
2) Leverage & Financing
3) Risk Management - Asset Protection & Insurance, Trustee Work
4) Asset Management & Investing - Under www.qlvbrookfield.com
5) Tax Efficient Strategies

Our Company Mark is a Pentagon with a key in the middle. A pentagon is the most efficient defensive structure. Each point of a pentagon is equal distance front every point . Each side provides support to another and works together, which is the key to our clients success.

Our key colors are blue, black and silver.

We ‘re located in the Pacific Northwest with bi coastal and international clients. We have fewer, higher net worth clients and provide exceptional customer service. We do not do social media.

website is www.harrowgatepath.com

Target Market(s)

High End Clients

Contact Information for Business Card

extra thick

Font styles to use
Serif

Requirements
Must have
• Metalic foil for lettering.
Black Background on one side
White Background on the other
Horizontal Format Only
No Rounded corners
Not Marketing sales information on the card.
Nice to have
• imprinted texture on the card
Should not have
• lots of color

```html
<!DOCTYPE html>
<html lang="en">
<head>
<meta charset="utf-8">
<title>Harrowgate Advisory – Business Card</title>
<link rel="stylesheet" href="https://fonts.googleapis.com/css2?family=Cinzel:wght@500&family=Arimo:wght@400&display=swap">
<style>
  :root {
    --backdrop: #0c0c0d;
    --card: #1a1a1b;
    --card-edge: #0e0e0f;
    --deep-ink: #050505;
    --navy: #0b2a78;
    --blue: #1d8fd8;
    --silver: #d4d6d9;
    --rule: #4a4a4c;
  }
  * { box-sizing: border-box; margin: 0; padding: 0; }
  html, body {
    width: 1200px; height: 900px; overflow: hidden;
    background: var(--backdrop);
  }
  .sheet {
    position: relative; width: 1200px; height: 900px;
    display: flex; flex-direction: column; align-items: center; justify-content: center;
    gap: 48px;
  }
  .card {
    position: relative; width: 630px; height: 360px;
    background: var(--card);
    border-bottom: 7px solid var(--navy);
    box-shadow: 0 10px 30px rgba(0,0,0,.7);
  }
  /* front */
  .card--front { display: flex; align-items: center; justify-content: center; }
  .front-mark {
    font-family: "Cinzel", serif; font-weight: 500;
    font-size: 34px; letter-spacing: 4px;
    color: var(--deep-ink);
    text-transform: uppercase;
  }
  /* back */
  .card--back { display: flex; }
  .brand {
    width: 46%; display: flex; align-items: center; justify-content: center;
  }
  .brand-name {
    font-family: "Cinzel", serif; font-weight: 500;
    font-size: 30px; line-height: 1.15; letter-spacing: 2px;
    color: var(--navy); text-align: center; text-transform: uppercase;
  }
  .divider {
    width: 1px; margin: 40px 0 36px; background: var(--rule);
  }
  .contact {
    flex: 1; padding: 70px 0 0 30px; color: var(--silver);
    font-family: "Arimo", sans-serif;
  }
  .person-name {
    font-family: "Cinzel", serif; font-weight: 500;
    font-size: 23px; letter-spacing: 1px; color: var(--blue);
    text-transform: uppercase; line-height: 1;
  }
  .person-title { font-size: 17px; margin: 6px 0 12px; }
  .contact-list { list-style: none; font-size: 17px; line-height: 1.5; }
  .contact-list li { display: flex; align-items: center; gap: 8px; }
  .contact-list svg { width: 15px; height: 15px; flex: none; }
  .address { font-size: 17px; line-height: 1.4; margin-top: 8px; }
</style>
</head>
<body>
<main class="sheet">
  <section class="card card--front" aria-label="Card front">
    <p class="front-mark">Harrowgate Advisory</p>
  </section>

  <section class="card card--back" aria-label="Card back">
    <div class="brand">
      <p class="brand-name">Harrowgate<br>Advisory</p>
    </div>
    <div class="divider"></div>
    <div class="contact">
      <h1 class="person-name">Corwin Ashdale</h1>
      <p class="person-title">Financial Strategist and Founder</p>
      <ul class="contact-list">
        <li>
          <svg viewBox="0 0 16 16" aria-hidden="true"><path d="M4 1.5l2.2 3-1.3 1.6c.9 2 2.5 3.6 4.4 4.5l1.6-1.3 3 2.2-1.2 2.4C6.8 14 2 9.2 1.6 3z" fill="none" stroke="var(--blue)" stroke-width="1.4" stroke-linejoin="round"/></svg>
          (503) 555-0147
        </li>
        <li>
          <svg viewBox="0 0 16 16" aria-hidden="true"><rect x="1" y="3" width="14" height="10" fill="var(--blue)"/><path d="M1 3l7 5.5L15 3" fill="none" stroke="var(--card)" stroke-width="1.3"/></svg>
          info@harrowgatepath.com
        </li>
        <li>
          <svg viewBox="0 0 16 16" aria-hidden="true"><g fill="none" stroke="var(--blue)" stroke-width="1.2"><circle cx="8" cy="8" r="6.5"/><ellipse cx="8" cy="8" rx="3" ry="6.5"/><path d="M1.5 8h13M2.5 4.8h11M2.5 11.2h11"/></g></svg>
          www.harrowgatepath.com
        </li>
      </ul>
      <p class="address">1480 Alder Crest Ave, Suite 312,<br>Portland, OR 97205</p>
    </div>
  </section>
</main>
</body>
</html>
```